GUARANTEED WordPress design needed for a sassy, confident charisma coach!

We need a website design for Marla Penrick's brand new, responsive, Wordpress website.
Marla is a trainer / coach who teaches people how to be more charismatic and runs events, publishes video courses and has an ongoing video blog. Her old website is here: www.marlapenrick.co.uk ... but it's now time to have a much better site!
We have a strong idea about the technical components of the website, but we need a designer's eye to create a great style for the site (and provide layered PSD files which our developers will then convert to HTML and CSS).
Marla's brand is sassy, brave, warm and confident. The videos on her existing site give quite a good feel for her personality. We need a clean, stylish and compelling page that isn't too corporate and captures her personality. Every element needs to feel coherent, from fonts and headings to colours and spacing.
The following sites are not exactly what Marla wants (and certainly aren't right in terms of colours) but they give you an idea of the kind of people she is competing against and the area she is operating in:
http://www.tessa-broughley.example/
http://rowanfelsby.example/
Ideally, you will have done something similar and be able to key in on exactly the kind of thing we want: we're not looking to reinvent the wheel. Hopefully you won't mind tweaking a few things if you are close to what we need.
More detail is provided in the word document attached. But in a nutshell we need: a banner, footer, sign-up strap, menu bar, signature and 4 different basic page types. We want bursts of bright colours, contrasted with black and white if possible - sorry we can't be more specific than that...
The word doc also contains some amateur mock-ups as well (the images are also just mockups at this stage) - but although these give a general sense of the structure what we are looking for, we are clearly not designers...so please help! We need a designer's touch!
Kind regards,
Corin
PS The layered PSD versions of the mockup files are available on Cloudvantre: https://files.cloudvantre.example/sh/k72pqa4w1zbtmrd/QXvenlr8Ty3PwMiU6Hs2kYfDb?dl=0
Target Market(s)
Entrepreneurs who need to sell themselves.
Number of Pages Required
4 page

```html
<!DOCTYPE html>
<html lang="en">
<head>
<meta charset="utf-8">
<title>Marla Penrick – Charisma Coach</title>
<link href="https://fonts.googleapis.com/css2?family=Raleway:wght@300;400;500;600;700;800&display=swap" rel="stylesheet">
<style>
:root{
  --ink:#2f2f2f;
  --header:#3b3b3b;
  --red:#d0101c;
  --red-dark:#a80c15;
  --yellow:#f7b500;
  --sky:#29b5e8;
  --mist:#ececec;
  --soft:#f5f5f5;
  --grey:#8a8a8a;
  --white:#ffffff;
  --photo-warm:#d9c7bd;
  --photo-cool:#c9ced6;
}
*{box-sizing:border-box;margin:0;padding:0}
html,body{width:1200px;height:2308px;overflow:hidden}
body{font-family:"Raleway",Arial,sans-serif;color:var(--ink);background:var(--white);position:relative}
section,header,footer{position:absolute;left:0;width:1200px}

/* header */
.site-header{top:0;height:88px;background:var(--header);display:flex;align-items:center;justify-content:space-between;padding:0 40px}
.brand{color:var(--white);font-weight:600;font-size:30px;letter-spacing:.5px;display:flex;align-items:center;gap:12px}
.brand-dot{width:14px;height:14px;border-radius:50%;background:var(--red)}
.main-nav{display:flex;gap:38px;height:88px;align-items:center}
.main-nav a{color:var(--white);text-decoration:none;font-size:15px;font-weight:500;letter-spacing:1px;height:88px;display:flex;align-items:center;border-bottom:4px solid transparent}
.main-nav a.current{border-bottom-color:var(--red);color:#ff6b70}

/* hero */
.hero{top:88px;height:644px;background:var(--white);overflow:hidden}
.hero-words{position:absolute;left:330px;top:218px;display:flex;flex-direction:column;gap:14px}
.hero-words span{display:inline-block;background:#2b2b2b;color:var(--red);font-size:50px;font-weight:500;letter-spacing:6px;padding:2px 22px;line-height:1.15;width:max-content}
.hero-portrait{position:absolute;left:730px;top:0;width:300px;height:644px;background:linear-gradient(180deg,#eadfd9 0%,#d8434a 45%,#c51923 100%);border-radius:150px 150px 0 0}
.slide-arrow{position:absolute;top:440px;width:48px;height:48px;border-radius:50%;background:#e6e6e6;display:flex;align-items:center;justify-content:center}
.slide-arrow.prev{left:18px}.slide-arrow.next{right:18px}

/* training band */
.training{top:732px;height:260px;background:var(--red)}
.laptop{position:absolute;left:150px;top:20px}
.training-copy{position:absolute;left:510px;top:42px;width:640px;color:var(--white)}
.training-copy h2{font-size:27px;font-weight:600;line-height:1.32}
.training-copy h2 strong{font-weight:800}
.signup-row{display:flex;gap:12px;margin-top:22px}
.field{background:var(--white);color:#9a9a9a;font-size:14px;height:42px;display:flex;align-items:center;padding:0 14px;width:230px}
.btn-yes{background:var(--yellow);color:var(--white);font-weight:700;font-size:15px;height:42px;padding:0 24px;display:flex;align-items:center}
.promise{font-size:13px;margin-top:10px;opacity:.9}

/* audiences */
.audiences{top:992px;height:330px;display:flex;justify-content:center;gap:40px;padding-top:60px}
.audience{width:520px;display:flex;gap:28px}
.audience-photo{width:210px;height:210px;border-radius:50%;flex:none}
.audience.individual .audience-photo{background:radial-gradient(circle at 40% 40%,var(--photo-warm),#8c6f62)}
.audience.business .audience-photo{background:radial-gradient(circle at 50% 40%,var(--photo-cool),#5a5f6b);order:2}
.audience h3{color:var(--red);font-size:26px;font-weight:600;margin:14px 0 10px}
.audience p{font-size:14px;line-height:1.55;color:#555}
.btn-red{display:inline-block;margin-top:18px;background:var(--red);color:var(--white);font-size:14px;font-weight:600;padding:10px 22px}
.divider{width:1px;background:#ddd;height:210px}

/* book band */
.book{top:1348px;height:212px;background:var(--sky)}
.book-badge{position:absolute;left:170px;top:26px;width:160px;height:160px;border-radius:50%;background:#e8463c;color:var(--white);font-size:28px;font-weight:700;display:flex;align-items:center;justify-content:center;letter-spacing:1px}
.book-copy{position:absolute;left:470px;top:52px;color:var(--white);font-size:34px;font-weight:500;line-height:1.3;width:620px}

/* testimonials */
.stories{top:1560px;height:300px;background:var(--soft)}
.stories-title{position:absolute;left:60px;top:96px;color:var(--grey);font-size:56px;font-weight:300;line-height:1.05}
.stories-title .quote{position:absolute;left:-26px;top:-70px;font-size:140px;color:#cfcfcf;font-weight:700}
.testimonial{position:absolute;left:420px;width:700px;display:flex;gap:22px}
.testimonial.first{top:44px}.testimonial.second{top:164px}
.avatar{width:74px;height:74px;border-radius:50%;flex:none;background:linear-gradient(135deg,#c8b2a3,#6f5a50)}
.testimonial p{font-size:13px;line-height:1.55;color:#555;font-style:normal}
.testimonial cite{display:block;margin-top:6px;font-style:normal;font-weight:700;font-size:13px;color:var(--ink)}

/* clients */
.clients{top:1860px;height:240px;background:var(--white);display:flex;align-items:center;justify-content:center;gap:48px}
.client{font-size:22px;font-weight:600;color:#555;display:flex;align-items:center;gap:8px}
.client-mark{width:14px;height:14px;background:#bbb}
.clients .slide-arrow{top:96px}

/* newsletter */
.newsletter{top:2100px;height:160px;background:var(--mist);text-align:center;padding-top:22px}
.newsletter p{font-size:17px;font-weight:500;line-height:1.45;color:var(--ink)}
.newsletter .signup-row{justify-content:center;margin-top:14px}
.newsletter .field{border:1px solid #ddd;height:34px}
.newsletter .btn-yes{background:var(--red);height:34px}
.socials{display:flex;justify-content:center;gap:8px;margin-top:10px;align-items:center;font-size:11px;color:#666}
.socials i{width:18px;height:18px;border-radius:50%;background:#666;display:inline-block}

/* footer */
.site-footer{top:2260px;height:48px;background:var(--white);display:flex;align-items:center;justify-content:center;gap:36px;font-size:12px;color:#777;letter-spacing:.5px}
</style>
</head>
<body>

<header class="site-header">
  <div class="brand"><span class="brand-dot"></span>Marla Penrick</div>
  <nav class="main-nav">
    <a class="current" href="#">EVENTS</a>
    <a href="#">WORK WITH ME</a>
    <a href="#">CORPORATE</a>
    <a href="#">ABOUT</a>
    <a href="#">CONTACT</a>
  </nav>
</header>

<section class="hero">
  <div class="hero-words"><span>ATTRACT</span><span>CONNECT</span><span>INFLUENCE</span></div>
  <div class="hero-portrait" role="img" aria-label="Photo of Marla in a red jumpsuit, posing confidently"></div>
  <div class="slide-arrow prev"><svg width="14" height="20" viewBox="0 0 14 20"><path d="M11 2 3 10l8 8" fill="none" stroke="#999" stroke-width="3"/></svg></div>
  <div class="slide-arrow next"><svg width="14" height="20" viewBox="0 0 14 20"><path d="M3 2l8 8-8 8" fill="none" stroke="#999" stroke-width="3"/></svg></div>
</section>

<section class="training">
  <svg class="laptop" width="310" height="220" viewBox="0 0 310 220">
    <rect x="25" y="0" width="260" height="180" rx="10" fill="#d7d7d7"/>
    <rect x="35" y="10" width="240" height="160" fill="#bfa79b"/>
    <rect x="0" y="182" width="310" height="14" rx="6" fill="#e2e2e2"/>
  </svg>
  <div class="training-copy">
    <h2>Learn how to unlock the superpower* of your charisma and win all the business you want with this <strong>FREE</strong> training</h2>
    <div class="signup-row">
      <div class="field">First Name</div>
      <div class="field">Email Address</div>
      <div class="btn-yes">YES PLEASE!</div>
    </div>
    <div class="promise">*Promise to only use your powers for good</div>
  </div>
</section>

<section class="audiences">
  <article class="audience individual">
    <div class="audience-photo" role="img" aria-label="Photo of a professional woman smiling"></div>
    <div>
      <h3>Individual</h3>
      <p>You are a professional who is frustrated with your image. You want nothing good to be easy, but don't know where to start.</p>
      <span class="btn-red">Make image work</span>
    </div>
  </article>
  <div class="divider"></div>
  <article class="audience business">
    <div>
      <h3>Business</h3>
      <p>You are a medium to large sized business which wants your employees to project a more confident professional image.</p>
      <span class="btn-red">Sort your staff out</span>
    </div>
    <div class="audience-photo" role="img" aria-label="Photo of a team at a corporate workshop"></div>
  </article>
</section>

<section class="book">
  <div class="book-badge">BOOK NOW</div>
  <div class="book-copy">And get the whole programme PLUS your own personalised notes for £397 (value £697)</div>
</section>

<section class="stories">
  <h2 class="stories-title"><span class="quote">“</span>Success<br>Stories</h2>
  <blockquote class="testimonial first">
    <div class="avatar" role="img" aria-label="Portrait of Mirela"></div>
    <div><p>“I've never been a fashionista and my wardrobe was dominated by the colour black… my appearance in terms of make up and clothing had become dull and uninteresting. One day with you and I was transformed, and my team noticed straight away.”</p><cite>Mirela – HR Director</cite></div>
  </blockquote>
  <blockquote class="testimonial second">
    <div class="avatar" role="img" aria-label="Portrait of Elspeth"></div>
    <div><p>“I booked you for a 1 to 1 image session. You soon had me feeling relaxed and confident about the colours and shapes that suit me, and the simple tips made getting ready each morning a pleasure. I would recommend you to anyone.”</p><cite>Elspeth – Director</cite></div>
  </blockquote>
</section>

<section class="clients">
  <div class="slide-arrow prev"><svg width="14" height="20" viewBox="0 0 14 20"><path d="M11 2 3 10l8 8" fill="none" stroke="#999" stroke-width="3"/></svg></div>
  <div class="client"><span class="client-mark"></span>Halvorne</div>
  <div class="client">Femmeforth</div>
  <div class="client">Ostbrück Bank</div>
  <div class="client">Pampero Grill</div>
  <div class="client">Lumenspire</div>
  <div class="client">Northwyn</div>
  <div class="slide-arrow next"><svg width="14" height="20" viewBox="0 0 14 20"><path d="M3 2l8 8-8 8" fill="none" stroke="#999" stroke-width="3"/></svg></div>
</section>

<section class="newsletter">
  <p>Hey! Don't go without signing up because you'll miss out on exclusive offers,<br>awesome tips, and weekly motivation in my fab newsletter!</p>
  <div class="signup-row">
    <div class="field">First Name</div>
    <div class="field">Email Address</div>
    <div class="btn-yes">YES PLEASE!</div>
  </div>
  <div class="socials">Find Marla's video feed <i></i><i></i><i></i><i></i><i></i></div>
</section>

<footer class="site-footer">
  <span>© Marla Penrick 2016</span><span>PRIVACY POLICY</span><span>TERMS POLICY</span><span>COOKIE POLICY</span><span>CONTACT</span>
</footer>

</body>
</html>
```